Fieldcrafters new logo business card

We need a business card designed to promote the new direction of our company. Originally (for the past 12 years) we were a design-based marketing consultancy specialising in B2B. But now we are offering marketing consultancy to companies in the ecommerce business. We have expertise in this and operate three online stores ourselves and can provide warehousing and distribution services.
The new logo and business card should reflect this market - e.g. modern, technical, commercial but also creative!
Our current logo is too 'designery' and doesn't reflect the seriousness and professionalism of our current business. It also is very long and thin so doesnot work well in rectangular panels.
The name 'Fieldcrafters' comprises two parts - Field and Crafters and these parts of the word can have a different type font or colour. The 'Field' element is the creative element while the 'Crafters' part is the technical, businesslike part. We can also look at 'The Fieldcrafters Company' rather than just 'fieldcrafters.' We can also include the slogan 'Source, Sell, Succeed.' under the logo.
The address details for the card are 4 Wrenfold Rise, Woking, Surrey GU19 3LT. We will also need an email address and phone number (details will be supplied later)
On the back of the card will be a list of services offered.
Fieldcrafters can help your business succeed through:
Product Sourcing
Marketing
Distribution
Storage
Ecommerce

Target Market(s)

Owners of small and medium-sized retail businesses - particularly mail order and ecommerce based businesses.

Industry/Entity Type

Marketing

Requirements
Must have
• The company name should be prominent. This can either be 'Fieldcrafters' or 'The Fieldcrafters Company'.
• Then the words 'Fieldcrafters Ltd, Unit F, Marlow Vale Park, Copperleaf Road, Elmstead, Woking, Surrey GU21 4RB
• 0844 312 9087 www.thefieldcrafters-example.co.uk
• Must also include cardholder's name and title.
• Martin Hollis
• Director
• On the reverse it should say.
• Fieldcrafters - Developing profitable brands in a multi-channel environment

```html
<!DOCTYPE html>
<html lang="en">
<head>
<meta charset="utf-8">
<title>Fieldcrafters Business Card</title>
<link rel="stylesheet" href="https://fonts.googleapis.com/css2?family=Cinzel:wght@600&family=Open+Sans:ital,wght@0,400;1,400;1,700&display=swap">
<style>
  :root {
    --bg: #e9e9e9;
    --card-top: #ffffff;
    --card-fade: #ececec;
    --sky: #1ba7e4;
    --navy: #3a3a9c;
    --ink: #2b2b2b;
    --white: #ffffff;
  }
  * { margin: 0; padding: 0; box-sizing: border-box; }
  html, body {
    width: 1200px; height: 901px; overflow: hidden;
    background: var(--bg);
  }
  .business-card {
    position: absolute; left: 100px; top: 165px;
    width: 1000px; height: 571px;
    border-radius: 48px; overflow: hidden;
    background: radial-gradient(ellipse at 30% 20%, var(--card-top) 40%, var(--card-fade) 100%);
    box-shadow: 0 8px 24px rgba(0,0,0,0.18);
    font-family: "Open Sans", Arial, sans-serif;
    color: var(--ink);
  }
  .card-waves { position: absolute; inset: 0; width: 100%; height: 100%; }
  .address {
    position: absolute; left: 70px; top: 50px;
    font-size: 24px; line-height: 1.3;
  }
  .contact-list {
    position: absolute; left: 60px; top: 168px;
    list-style: none; font-size: 23px; line-height: 1.32;
  }
  .contact-list li { display: flex; align-items: center; gap: 10px; }
  .contact-list svg { width: 20px; height: 20px; fill: var(--navy); flex: none; }
  .company-name {
    position: absolute; right: 100px; top: 300px;
    font-family: "Cinzel", Georgia, serif; font-weight: 600;
    font-size: 54px; letter-spacing: 1px; color: var(--navy);
  }
  .cardholder {
    position: absolute; right: 70px; bottom: 36px;
    text-align: right; color: var(--white);
  }
  .cardholder-name { font-size: 28px; font-style: italic; font-weight: 700; }
  .cardholder-title { font-size: 27px; font-style: italic; font-weight: 400; }
</style>
</head>
<body>
  <div class="business-card">
    <svg class="card-waves" viewBox="0 0 1000 571" preserveAspectRatio="none" aria-hidden="true">
      <path d="M280 405 C500 445 760 440 1000 428 L1000 446 C760 456 500 452 280 405 Z" fill="var(--navy)"/>
      <path d="M0 325 C200 420 520 472 1000 462 L1000 571 L0 571 Z" fill="var(--sky)"/>
    </svg>

    <p class="address">Fieldcrafters Ltd, Unit F, Marlow Vale Park<br>Copperleaf Road, Elmstead<br>Woking, Surrey GU21 4RB</p>

    <ul class="contact-list">
      <li><svg viewBox="0 0 20 20"><rect x="2" y="6" width="16" height="11" rx="2"/><rect x="5" y="2" width="10" height="5" rx="1"/></svg>0844 312 9087</li>
      <li><svg viewBox="0 0 20 20"><path d="M5 2 L8 2 L9 6 L7 8 C8 11 9 12 12 13 L14 11 L18 12 L18 15 C18 17 16 18 14 18 C8 17 3 12 2 6 C2 4 3 2 5 2 Z"/></svg>0844 312 9087</li>
      <li><svg viewBox="0 0 20 20"><rect x="1" y="4" width="18" height="12" rx="1"/><path d="M2 5 L10 11 L18 5" stroke="#fff" stroke-width="1.5" fill="none"/></svg>info@thefieldcrafters-example.co.uk</li>
      <li><svg viewBox="0 0 20 20"><circle cx="10" cy="10" r="8"/><path d="M2 10 H18 M10 2 C6 6 6 14 10 18 M10 2 C14 6 14 14 10 18" stroke="#fff" stroke-width="1.2" fill="none"/></svg>www.thefieldcrafters-example.co.uk</li>
    </ul>

    <div class="company-name">Fieldcrafters</div>

    <div class="cardholder">
      <p class="cardholder-name">Dara Quillfen</p>
      <p class="cardholder-title">Consultant</p>
    </div>
  </div>
</body>
</html>
```